Bref créative
Valtoni Building and Design Stationary
Valtoni Building & Design
Professional
Martin K. Valtoni
President / Owner
4172 Wexmoor Avenue
Suite 2807
Corvale Heights, ME 07319
mkvaltoni@valtonibuilding.example
www.valtonibuilding.example
The logo, which will be uploaded.
Logo for the back of card. Please show us versions with both black background and white background.
Logo with white background. Please show us versions for back of card with both black and white background.

```html
<!DOCTYPE html>
<html lang="en">
<head>
<meta charset="utf-8">
<title>Valtoni Building &amp; Design — Business Cards</title>
<link href="https://fonts.googleapis.com/css2?family=Lato:wght@400;700&display=swap" rel="stylesheet">
<style>
  :root {
    --backdrop: #2b2d30;
    --card-white: #ffffff;
    --brand-red: #c4161c;
    --red-deep: #7d0c10;
    --red-light: #e0282e;
    --divider: #3b3b3d;
    --ink-light: #ffffff;
    --ink-soft: #f3d4d5;
  }
  * { margin: 0; padding: 0; box-sizing: border-box; }
  html, body { width: 1200px; height: 852px; overflow: hidden; }
  body {
    background: var(--backdrop);
    font-family: "Lato", Arial, sans-serif;
    position: relative;
  }
  .card {
    position: absolute;
    width: 520px;
    height: 300px;
    border-radius: 16px;
    overflow: hidden;
    background: var(--card-white);
    box-shadow: 0 10px 30px rgba(0,0,0,0.45);
  }
  .card--left-panel { left: 60px; top: 130px; }
  .card--right-panel { left: 620px; top: 420px; }
  .card-shapes { position: absolute; inset: 0; width: 100%; height: 100%; }

  .contact {
    position: absolute;
    top: 26px;
    width: 280px;
    color: var(--ink-light);
  }
  .card--left-panel .contact { left: 26px; }
  .card--right-panel .contact { right: 26px; text-align: right; }

  .contact-name { font-size: 19px; font-weight: 700; letter-spacing: 0.2px; }
  .contact-title { font-size: 12.5px; color: var(--ink-soft); margin-top: 2px; }
  .contact-address { font-size: 12px; line-height: 1.45; margin-top: 70px; }
  .contact-lines { list-style: none; font-size: 11.5px; line-height: 1.7; margin-top: 12px; }
  .contact-lines li { display: flex; align-items: center; gap: 7px; }
  .card--right-panel .contact-lines li { flex-direction: row-reverse; justify-content: flex-start; }
  .contact-icon { width: 11px; height: 11px; flex: none; }

  .brand {
    position: absolute;
    top: 50%;
    transform: translateY(-50%);
    width: 170px;
    display: flex;
    flex-direction: column;
    align-items: center;
    gap: 10px;
    text-align: center;
  }
  .card--left-panel .brand { right: 22px; }
  .card--right-panel .brand { left: 28px; }
  .brand-dot {
    width: 46px; height: 46px; border-radius: 50%;
    background: var(--brand-red);
  }
  .brand-name {
    font-size: 19px;
    font-weight: 700;
    line-height: 1.2;
    color: var(--brand-red);
  }
</style>
</head>
<body>

<section class="card card--left-panel">
  <svg class="card-shapes" viewBox="0 0 520 300" preserveAspectRatio="none" aria-hidden="true">
    <defs>
      <radialGradient id="redGlowA" cx="0.35" cy="0.4" r="0.8">
        <stop offset="0" stop-color="var(--red-light)"/>
        <stop offset="0.55" stop-color="var(--brand-red)"/>
        <stop offset="1" stop-color="var(--red-deep)"/>
      </radialGradient>
    </defs>
    <path d="M0 0 H346 C300 100 300 200 346 300 H0 Z" fill="var(--divider)"/>
    <path d="M0 0 H332 C286 100 286 200 332 300 H0 Z" fill="url(#redGlowA)"/>
  </svg>
  <div class="contact">
    <div class="contact-name">Martin K. Valtoni</div>
    <div class="contact-title">President / Owner</div>
    <div class="contact-address">4172 Wexmoor Avenue<br>Suite 2807<br>Corvale Heights, ME 07319</div>
    <ul class="contact-lines">
      <li><svg class="contact-icon" viewBox="0 0 12 12"><path d="M3 1 L5 3.5 L4 5 C5 7 6 8 7.5 8.5 L9 7.5 L11 9.5 L9.5 11 C5 10.5 1.5 7 1 2.5 Z" fill="currentColor"/></svg>555-410-0148</li>
      <li><svg class="contact-icon" viewBox="0 0 12 12"><rect x="1" y="2.5" width="10" height="7" rx="1" fill="none" stroke="currentColor" stroke-width="1.2"/><path d="M1.5 3 L6 6.5 L10.5 3" fill="none" stroke="currentColor" stroke-width="1.2"/></svg>mkvaltoni@valtonibuilding.example</li>
      <li><svg class="contact-icon" viewBox="0 0 12 12"><circle cx="6" cy="6" r="4.8" fill="none" stroke="currentColor" stroke-width="1.2"/><path d="M1.2 6 H10.8 M6 1.2 C3.5 4 3.5 8 6 10.8 M6 1.2 C8.5 4 8.5 8 6 10.8" fill="none" stroke="currentColor" stroke-width="1"/></svg>www.valtonibuilding.example</li>
    </ul>
  </div>
  <div class="brand">
    <span class="brand-dot"></span>
    <span class="brand-name">Valtoni Building &amp; Design</span>
  </div>
</section>

<section class="card card--right-panel">
  <svg class="card-shapes" viewBox="0 0 520 300" preserveAspectRatio="none" aria-hidden="true">
    <defs>
      <radialGradient id="redGlowB" cx="0.65" cy="0.4" r="0.8">
        <stop offset="0" stop-color="var(--red-light)"/>
        <stop offset="0.55" stop-color="var(--brand-red)"/>
        <stop offset="1" stop-color="var(--red-deep)"/>
      </radialGradient>
    </defs>
    <path d="M520 0 H174 C220 100 220 200 174 300 H520 Z" fill="var(--divider)"/>
    <path d="M520 0 H188 C234 100 234 200 188 300 H520 Z" fill="url(#redGlowB)"/>
  </svg>
  <div class="contact">
    <div class="contact-name">Martin K. Valtoni</div>
    <div class="contact-title">President / Owner</div>
    <div class="contact-address">4172 Wexmoor Avenue<br>Suite 2807<br>Corvale Heights, ME 07319</div>
    <ul class="contact-lines">
      <li><svg class="contact-icon" viewBox="0 0 12 12"><path d="M3 1 L5 3.5 L4 5 C5 7 6 8 7.5 8.5 L9 7.5 L11 9.5 L9.5 11 C5 10.5 1.5 7 1 2.5 Z" fill="currentColor"/></svg>555-410-0148</li>
      <li><svg class="contact-icon" viewBox="0 0 12 12"><rect x="1" y="2.5" width="10" height="7" rx="1" fill="none" stroke="currentColor" stroke-width="1.2"/><path d="M1.5 3 L6 6.5 L10.5 3" fill="none" stroke="currentColor" stroke-width="1.2"/></svg>mkvaltoni@valtonibuilding.example</li>
      <li><svg class="contact-icon" viewBox="0 0 12 12"><circle cx="6" cy="6" r="4.8" fill="none" stroke="currentColor" stroke-width="1.2"/><path d="M1.2 6 H10.8 M6 1.2 C3.5 4 3.5 8 6 10.8 M6 1.2 C8.5 4 8.5 8 6 10.8" fill="none" stroke="currentColor" stroke-width="1"/></svg>www.valtonibuilding.example</li>
    </ul>
  </div>
  <div class="brand">
    <span class="brand-dot"></span>
    <span class="brand-name">Valtoni Building &amp; Design</span>
  </div>
</section>

</body>
</html>
```